Your complete Gardening and lawn maintenance, Horticultural care. (to be on card)
We are looking at using a logo of a tree, with a recycling emblem circling the tree. The colors of choice, are burnt oranges and olive greens. Presented; simple to the eye, yet catchy to the clients in a eco-friendly way. We have uploaded a design for you to look at just to give a rough idea, you can use that or create your own ideas or play around with a mixture.

Target Market(s)

Home owners, businesses, real estates.

Industry/Entity Type

Recycling

Contact Information for Business Card

Name: Colin Breversted
Phone: 0438159027
Email: brightmossyards@mailbarn.net

Logo Text

Bright-Moss Yards

Logo styles of interest
Emblem Logo
Pictorial/Combination Logo
Abstract Logo
Requirements
Must have
• Business name: Bright-Moss Yards
and slogan : Your complete Gardening and lawn maintenance, Horticultural care

```html
<!DOCTYPE html>
<html lang="en">
<head>
<meta charset="utf-8">
<title>Bright-Moss Yards – Business Card</title>
<link rel="stylesheet" href="https://fonts.googleapis.com/css2?family=Mulish:wght@400;700;800&display=swap">
<style>
  :root {
    --page: #e9ebe6;
    --olive: #6a9a3b;
    --olive-deep: #4f7f2c;
    --leaf-pale: rgba(255, 255, 255, 0.28);
    --arrow-pale: #a9c893;
    --burnt-orange: #e4561c;
    --card-white: #ffffff;
    --ink-white: #ffffff;
  }
  * { box-sizing: border-box; margin: 0; padding: 0; }
  html, body {
    width: 1200px; height: 900px; overflow: hidden;
    background: var(--page);
    font-family: "Mulish", Arial, sans-serif;
  }
  .canvas {
    position: relative; width: 1200px; height: 900px;
  }
  .card {
    position: absolute; left: 330px;
    width: 540px; height: 310px;
    border-radius: 18px; overflow: hidden;
    box-shadow: 0 6px 18px rgba(0,0,0,0.18);
  }

  /* Front side */
  .card--front { top: 110px; background: var(--olive); }
  .leaf-spray {
    position: absolute;
    background: radial-gradient(ellipse at center, var(--leaf-pale) 0%, rgba(255,255,255,0.08) 70%, transparent 100%);
  }
  .leaf-spray--left { left: -20px; top: 60px; width: 120px; height: 170px; }
  .leaf-spray--right { right: -20px; top: -10px; width: 110px; height: 110px; }
  .front-brand {
    position: absolute; left: 0; right: 0; top: 86px;
    display: flex; align-items: center; justify-content: center; gap: 10px;
  }
  .brand-dot {
    width: 16px; height: 16px; border-radius: 50%;
    background: var(--ink-white);
  }
  .brand-name {
    font-weight: 800; font-size: 26px; letter-spacing: 0.5px;
    color: var(--ink-white);
  }
  .tagline {
    position: absolute; left: 0; right: 0; top: 198px;
    text-align: center; color: var(--ink-white);
    font-weight: 700; font-size: 13.5px; line-height: 1.45;
    letter-spacing: 0.6px; text-transform: uppercase;
  }

  /* Back side */
  .card--back { top: 480px; background: var(--card-white); }
  .motif {
    position: absolute; right: 0; top: 0; width: 300px; height: 310px;
    background: radial-gradient(ellipse at 75% 55%, rgba(169,200,147,0.55) 0%, rgba(169,200,147,0.15) 55%, transparent 80%);
  }
  .back-brand {
    position: absolute; left: 34px; top: 132px;
    display: flex; align-items: center; gap: 8px;
  }
  .back-brand .brand-dot { background: var(--olive-deep); width: 14px; height: 14px; }
  .back-brand .brand-name { color: var(--olive-deep); font-size: 19px; }
  .contact {
    position: absolute; left: 272px; top: 112px;
    color: var(--burnt-orange);
  }
  .contact__name {
    font-weight: 800; font-size: 21px; letter-spacing: 0.8px;
    text-transform: uppercase; margin-bottom: 10px;
  }
  .contact__line { font-size: 14.5px; line-height: 1.4; }
</style>
</head>
<body>
  <main class="canvas">
    <section class="card card--front">
      <div class="leaf-spray leaf-spray--left" role="img" aria-label="Pale leaf spray decoration"></div>
      <div class="leaf-spray leaf-spray--right" role="img" aria-label="Pale leaf spray decoration"></div>
      <div class="front-brand">
        <span class="brand-dot"></span>
        <span class="brand-name">Bright-Moss Yards</span>
      </div>
      <p class="tagline">Your complete gardening<br>and lawn maintenance, horticultural care.</p>
    </section>

    <section class="card card--back">
      <div class="motif" role="img" aria-label="Soft green background decoration"></div>
      <div class="back-brand">
        <span class="brand-dot"></span>
        <span class="brand-name">Bright-Moss Yards</span>
      </div>
      <div class="contact">
        <p class="contact__name">Colin Breversted</p>
        <p class="contact__line">0438159027</p>
        <p class="contact__line">brightmossyards@mailbarn.net</p>
      </div>
    </section>
  </main>
</body>
</html>
```